landscaping core flute signs

I need core flutes created with business name and a few extra dot points for putting on fences for job sites 120cm x 120cm approx.
I want our old ones information with the new L logo and colour palette

```html
<!DOCTYPE html>
<html lang="en">
<head>
<meta charset="utf-8">
<title>Terrafirm Grounds – Site Sign</title>
<link rel="stylesheet" href="https://fonts.googleapis.com/css2?family=Bebas+Neue&family=Montserrat:wght@500;700;800&display=swap">
<style>
  :root {
    --ink: #050608;
    --leaf: #638f5a;
    --leaf-deep: #3f6133;
    --leaf-mid: #4b7541;
    --paper: #f6f6f6;
  }
  * { box-sizing: border-box; margin: 0; padding: 0; }
  html, body { width: 1190px; height: 1200px; overflow: hidden; background: var(--ink); }
  .sign {
    position: relative;
    width: 1190px;
    height: 1200px;
    background: var(--ink);
    overflow: hidden;
    font-family: "Bebas Neue", "Oswald", sans-serif;
  }
  .licence {
    position: absolute;
    left: 60px; top: 59px;
    height: 32px;
    display: flex;
    border-radius: 16px;
    background: var(--paper);
    font-family: "Montserrat", sans-serif;
    font-weight: 700;
    font-size: 24px;
    letter-spacing: 2px;
    line-height: 32px;
    overflow: hidden;
  }
  .licence-label { color: var(--ink); padding: 0 6px 0 10px; }
  .licence-number { color: var(--paper); background: var(--leaf); padding: 0 12px 0 10px; border-radius: 16px; }
  .brand {
    position: absolute;
    left: 0; right: 0; top: 120px;
    display: flex;
    flex-direction: column;
    align-items: center;
    gap: 34px;
  }
  .brand-dot { width: 220px; height: 220px; border-radius: 50%; background: var(--leaf); }
  .brand-name {
    color: var(--paper);
    font-size: 120px;
    line-height: 1;
    letter-spacing: 4px;
  }
  .services {
    position: absolute;
    left: 0; right: 0; top: 640px;
    display: grid;
    grid-template-columns: 1fr 1fr 1fr;
    padding: 0 72px;
  }
  .service {
    text-align: center;
    font-size: 82px;
    line-height: 74px;
    padding-top: 6px;
  }
  .service + .service { border-left: 3px solid var(--leaf); }
  .service-top { display: block; color: var(--paper); }
  .service-bottom { display: block; color: var(--leaf); }
  .chevron { position: absolute; left: 0; top: 0; }
  .contact {
    position: absolute;
    left: 0; right: 0; top: 968px;
    display: flex;
    flex-direction: column;
    align-items: center;
    gap: 14px;
  }
  .phone {
    font-family: "Montserrat", sans-serif;
    font-weight: 800;
    font-size: 128px;
    line-height: 1;
    color: var(--paper);
    letter-spacing: -1px;
  }
  .email {
    display: flex;
    align-items: center;
    gap: 8px;
    height: 58px;
    padding: 0 22px;
    border: 2px solid var(--ink);
    border-radius: 29px;
    font-family: "Montserrat", sans-serif;
    font-weight: 500;
    font-size: 40px;
    letter-spacing: 3px;
    color: var(--ink);
  }
</style>
</head>
<body>
<main class="sign">
  <div class="licence"><span class="licence-label">QBSA</span><span class="licence-number">1098234</span></div>

  <header class="brand">
    <div class="brand-dot"></div>
    <h1 class="brand-name">TERRAFIRM GROUNDS</h1>
  </header>

  <section class="services">
    <p class="service"><span class="service-top">PAVING &amp;</span><span class="service-bottom">CONCRETING</span></p>
    <p class="service"><span class="service-top">FENCING</span><span class="service-bottom">&amp; RETAINING</span></p>
    <p class="service"><span class="service-top">DESIGN &amp;</span><span class="service-bottom">CONSTRUCT</span></p>
  </section>

  <svg class="chevron" width="1190" height="1200" viewBox="0 0 1190 1200" aria-hidden="true">
    <polygon points="0,771 595,934 1190,771 1190,1200 0,1200" fill="var(--leaf-deep)"/>
    <polygon points="595,934 1190,771 1190,806 660,952" fill="var(--leaf-mid)"/>
    <polygon points="0,806 595,970 1190,806 1190,1200 0,1200" fill="var(--leaf)"/>
  </svg>

  <footer class="contact">
    <p class="phone">0412 555 208</p>
    <p class="email">
      <svg width="38" height="34" viewBox="0 0 38 34" aria-hidden="true">
        <rect x="2" y="10" width="34" height="22" rx="2" fill="none" stroke="var(--ink)" stroke-width="2.5"/>
        <polyline points="2,12 19,24 36,12" fill="none" stroke="var(--ink)" stroke-width="2.5"/>
        <rect x="10" y="1" width="18" height="15" fill="var(--leaf)" stroke="var(--ink)" stroke-width="2"/>
        <circle cx="19" cy="8.5" r="3.5" fill="none" stroke="var(--ink)" stroke-width="1.8"/>
      </svg>
      sam@terrafirmgrounds.com
    </p>
  </footer>
</main>
</body>
</html>
```